Verpackungen für kleine Imkerei
Zielgruppe
Wir sind eine kleine Imkerei aus dem Aargau (Schweiz) und stellen zusammen mit unseren glücklichen Bienen feinsten Honig her. Gerne möchten wir unseren visuelle Kommunikation nach aussen mit Hilfe eines neuen Etiketts verbessern.
Aufgabenstellung
Das Etikett muss rechteckig sein und wir auf einem runden Glas aufgeklebt. Die Maximalgrösse ist 210x45mm (beim 500g Glas) und entsprechend kleiner bei kleineren Einheiten. Wir möchten ein Grunddesign, welches adaptierbar ist auf die weiteren Sorten. (Waldhonig, Blütenhonig, cremiger Blütenhonig, Zürcher Stadthonig, Badener Stadthonig, Lenzburger Stadthonig). Barcode muss keinen eingefügt werden, nur die gesetzlichen Daten müssen auf dem Etiektt stehen. Weitere Wünsche und Anmerkungen befinden sich im pdf.
Sollten Dateien oder Bilder nachgereicht werden, bitte melden!

```html
<!DOCTYPE html>
<html lang="de">
<head>
<meta charset="utf-8">
<title>Sonnwabe – Blütenhonig Etikett</title>
<link rel="stylesheet" href="https://fonts.googleapis.com/css2?family=Roboto:wght@300;400&family=Roboto+Condensed:wght@400;500;700&display=swap">
<style>
  :root {
    --paper: #ffffff;
    --ink: #1d1d1b;
    --rule: #8a8a8a;
    --frame: #c8c8c8;
    --honey: #f6b221;
    --honey-soft: #fbd48a;
    --honey-pale: #fdebc4;
    --field: #fde9c6;
  }
  * { box-sizing: border-box; margin: 0; padding: 0; }
  html, body {
    width: 1200px; height: 288px; overflow: hidden;
    background: var(--paper);
  }
  .canvas { position: relative; width: 1200px; height: 288px; background: var(--paper); }

  .label {
    position: absolute; left: 20px; top: 20px; width: 1161px; height: 247px;
    border: 1px solid var(--frame); background: var(--paper); overflow: hidden;
  }

  /* Left info column */
  .info { position: absolute; left: 21px; top: 0; width: 184px; color: var(--ink);
    font-family: "Roboto", Arial, sans-serif; font-weight: 400; }
  .info__origin { position: absolute; top: 16px; left: 0;
    font-family: "Roboto Condensed", Arial, sans-serif; font-weight: 500;
    font-size: 12.5px; letter-spacing: 2.6px; white-space: nowrap; }
  .info__rule { position: absolute; left: 0; width: 184px; height: 1px; background: var(--rule); }
  .info__rule--top { top: 36px; }
  .info__rule--mid { top: 113px; }
  .info__address { position: absolute; top: 41px; left: 0; font-style: normal;
    font-size: 12px; line-height: 17px; white-space: nowrap; }
  .info__storage { position: absolute; top: 118px; left: 0;
    font-size: 12px; line-height: 17px; white-space: nowrap; }
  .info__codes { position: absolute; top: 176px; left: 0; display: flex; align-items: center;
    font-size: 9px; white-space: nowrap; }
  .info__field { display: inline-block; background: var(--field); padding: 4px 6px; height: 17px; line-height: 9px; }
  .info__field--date { width: 62px; }
  .info__field--lot { width: 56px; margin-left: 4px; }
  .info__lot-label { margin-left: 14px; }
  .info__weight { position: absolute; top: 204px; left: 0;
    font-family: "Roboto", Arial, sans-serif; font-weight: 300; font-size: 25px; line-height: 1; }

  /* Centre panel */
  .front { position: absolute; left: 312px; top: 0; width: 565px; height: 247px; }
  .front__artwork {
    position: absolute; left: 10px; top: -2px; width: 545px; height: 250px;
    background:
      radial-gradient(ellipse 42% 48% at 45% 45%, var(--honey-soft) 0%, rgba(251,212,138,0.75) 55%, rgba(253,235,196,0) 100%),
      radial-gradient(ellipse 30% 40% at 78% 42%, var(--honey-pale) 0%, rgba(253,235,196,0) 100%);
  }
  .front__tagline { position: absolute; top: 20px; left: 0; width: 430px; text-align: center;
    font-family: "Roboto", Arial, sans-serif; font-weight: 300; font-size: 12.5px;
    line-height: 15px; color: var(--ink); letter-spacing: 0.2px; }
  .front__brand { position: absolute; top: 82px; left: 0; width: 430px; text-align: center;
    font-family: "Roboto", Arial, sans-serif; font-weight: 300; font-size: 64px;
    line-height: 64px; color: var(--ink); }
  .front__variety { position: absolute; top: 212px; left: 0; width: 430px; text-align: center;
    font-family: "Roboto Condensed", Arial, sans-serif; font-weight: 700; font-size: 19px;
    line-height: 1; letter-spacing: 1.8px; color: var(--ink); }

  /* Right text panel */
  .notes { position: absolute; left: 1003px; top: 0; width: 142px; height: 247px;
    background: var(--honey); padding: 17px 8px 0 19px; }
  .notes__text { color: var(--paper); font-family: "Roboto", Arial, sans-serif; font-weight: 400;
    font-size: 11px; line-height: 15.2px; text-align: justify; hyphens: none; }
</style>
</head>
<body>
<div class="canvas">
  <div class="label">

    <section class="info">
      <p class="info__origin">SCHWEIZER HONIG</p>
      <span class="info__rule info__rule--top"></span>
      <address class="info__address">
        Andrea &amp; Lukas Brunner<br>
        Lindenweg 4<br>
        CH-5612 Wiesenau<br>
        www.sonnwabe.ch
      </address>
      <span class="info__rule info__rule--mid"></span>
      <p class="info__storage">
        Den Honig gut verschlossen,<br>
        trocken, dunkel, kühl bei max. 15º<br>
        lagern. Mindestens haltbar bis:
      </p>
      <div class="info__codes">
        <span class="info__field info__field--date">DD/MM/YY</span>
        <span class="info__lot-label">Lot-Nr:</span>
        <span class="info__field info__field--lot">LXXXXX</span>
      </div>
      <p class="info__weight">500g</p>
    </section>

    <section class="front">
      <div class="front__artwork" role="img" aria-label="Honiggelber Aquarellfleck mit gezeichneten Bienen, Blüten, Blättern und Punkten"></div>
      <p class="front__tagline">SCHWEIZER HONIG<br>VON GLÜCKLICHEN BIENEN</p>
      <p class="front__brand">sonnwabe</p>
      <p class="front__variety">BLÜTENHONIG</p>
    </section>

    <aside class="notes">
      <p class="notes__text">Lorem ipsum sit dolor sit amet, consectetuer adipiscing elit, sed diam nonummy nibh euismod tincidunt ut laoreet dolore magna aliquamar estes erat volutpat. Ut wisi enim ad minim veniam, est quis nostrud exerci tation ullam corper suscipit lobortis nisl ut os aliquip existed gradua lorem ipsum.</p>
    </aside>

  </div>
</div>
</body>
</html>
```